Bright, Fun and hard to forget home inspection business card.

We need a Business card design for a new Home Inspection company. We are building a brand that is bright, fun and easy to remember.

Target Market(s)

Anyone involed in buying and selling of homes.

Industry/Entity Type

Home Inspection

Contact Information for Business Card

Colin Marlowe Owner/Inspector

Wedsite- PorchAndRafterCheck.example
Phone: 253-555-0187
Email- ColinMarlowe@mailbox.example
WA Lic # 4806

Requirements
Must have
• BRQV LOGO somewhere on card.

```html
<!DOCTYPE html>
<html lang="en">
<head>
<meta charset="utf-8">
<title>Porch and Rafter Check – Business Card</title>
<link rel="stylesheet" href="https://fonts.googleapis.com/css2?family=Jost:ital,wght@0,400;0,700;1,400&display=swap">
<style>
  :root {
    --brand-orange: #f15a29;
    --ink: #111111;
    --paper: #ffffff;
    --badge-dark: #1a1a1a;
  }
  html, body {
    margin: 0;
    padding: 0;
    width: 1200px;
    height: 686px;
    overflow: hidden;
    background: var(--paper);
  }
  .card {
    position: relative;
    width: 1200px;
    height: 686px;
    background: var(--paper);
    overflow: hidden;
    font-family: "Jost", "Century Gothic", sans-serif;
  }
  .card__edge-band {
    position: absolute;
    top: 0; left: 0;
    width: 42px; height: 686px;
    background: var(--brand-orange);
  }
  .card__edge-stripe {
    position: absolute;
    top: 0; left: 62px;
    width: 10px; height: 686px;
    background: var(--brand-orange);
  }
  .card__brand-panel {
    position: absolute;
    inset: 0;
  }
  .card__text {
    position: absolute;
    left: 110px;
    margin: 0;
    white-space: nowrap;
    line-height: 1;
  }
  .person-name {
    top: 46px;
    font-size: 53px;
    font-weight: 700;
    color: var(--ink);
    letter-spacing: 0.5px;
  }
  .person-title {
    top: 114px;
    font-size: 32px;
    font-style: italic;
    color: var(--brand-orange);
  }
  .person-license {
    top: 163px;
    font-size: 32px;
    color: var(--brand-orange);
  }
  .certification-badge {
    position: absolute;
    left: 110px;
    top: 240px;
    width: 144px;
    height: 166px;
    background: var(--badge-dark);
  }
  .contact {
    font-size: 39px;
    color: var(--brand-orange);
    letter-spacing: 0.3px;
  }
  .contact--web { top: 461px; }
  .contact--phone { top: 530px; }
  .contact--email { top: 585px; }
  .brand-mascot {
    position: absolute;
    left: 668px;
    top: 69px;
    width: 212px;
    height: 245px;
    border-radius: 40px;
    background: linear-gradient(160deg, #f47a50 0%, #f15a29 100%);
  }
  .brand-name {
    position: absolute;
    left: 888px;
    top: 66px;
    width: 250px;
    margin: 0;
    color: var(--paper);
    font-weight: 400;
    text-transform: uppercase;
    line-height: 0.95;
  }
  .brand-name__line { display: block; }
  .brand-name__line--small { font-size: 30px; }
  .brand-name__line--large { font-size: 58px; letter-spacing: -1px; }
  .brand-name__line--tiny { font-size: 18px; text-align: right; padding-right: 50px; }
</style>
</head>
<body>
  <div class="card">
    <svg class="card__brand-panel" width="1200" height="686" viewBox="0 0 1200 686" aria-hidden="true">
      <polygon points="855,0 981,686 1200,686 1200,0" fill="var(--brand-orange)"/>
    </svg>
    <div class="card__edge-band"></div>
    <div class="card__edge-stripe"></div>

    <h1 class="card__text person-name">Colin Marlowe</h1>
    <p class="card__text person-title">Owner / Inspector</p>
    <p class="card__text person-license">WA Lic # 4806</p>

    <div class="certification-badge" role="img" aria-label="BRQV certification badge"></div>

    <p class="card__text contact contact--web">PorchAndRafterCheck.example</p>
    <p class="card__text contact contact--phone">253-555-0187</p>
    <p class="card__text contact contact--email">ColinMarlowe@mailbox.example</p>

    <div class="brand-mascot" role="img" aria-label="Brand mascot: cartoon inspector holding a megaphone"></div>
    <p class="brand-name">
      <span class="brand-name__line brand-name__line--small">Porch and</span>
      <span class="brand-name__line brand-name__line--large">Rafter</span>
      <span class="brand-name__line brand-name__line--large">Check</span>
      <span class="brand-name__line brand-name__line--tiny">LLC</span>
    </p>
  </div>
</body>
</html>
```